Velmor Stationery Design

We need Business Card, Letterhead, #10 Envelope , 3" x 4" Mailing Label, and email signature block. Also need "Aircraft Services" added small under the logo on everything except the email signature block. "Aircraft Services" should be in a simple font to to conflict with or distract from the logo. Our address info is:
4817 Halvend Loop NW
Brantwick, GA 30592
P 555.208.3146
C 555.208.3146 (for biz cards only)
glen@velmorjet.example (for biz cards only)
Website velmorjet.example
Feel free to play around with colors but I expect that black or gray will work best for the address/phone info etc.

Target Market(s)

Aircraft owners

Industry/Entity Type

Aviation

Colors

Designer to choose only greyscale colors for use in the design.

Requirements
Must have
• Clean and sophisticated design -

```html
<!DOCTYPE html>
<html lang="en">
<head>
<meta charset="utf-8">
<title>Velmor Stationery</title>
<link rel="stylesheet" href="https://fonts.googleapis.com/css2?family=Montserrat:wght@400;800&family=Open+Sans:wght@400;600&display=swap">
<style>
  :root {
    --brand-blue: #2a68c2;
    --paper: #ffffff;
    --backdrop: #e8e7e4;
    --ink: #2b2b2b;
    --ink-soft: #555555;
    --icon-box: #1e1e1e;
  }
  * { box-sizing: border-box; margin: 0; padding: 0; }
  html, body { width: 1200px; height: 900px; overflow: hidden; }
  body {
    background: var(--backdrop);
    font-family: "Open Sans", sans-serif;
    color: var(--ink);
    position: relative;
  }
  .sheet {
    position: absolute;
    background: var(--paper);
    box-shadow: 0 2px 8px rgba(0,0,0,0.12);
    overflow: hidden;
  }

  /* Brand lockup */
  .lockup { display: inline-flex; flex-direction: column; align-items: center; color: var(--brand-blue); }
  .lockup-name {
    font-family: "Montserrat", sans-serif;
    font-weight: 800;
    text-transform: uppercase;
    letter-spacing: 0.04em;
    line-height: 1;
  }
  .lockup-tagline {
    display: flex; align-items: center; gap: 6px;
    font-family: "Montserrat", sans-serif;
    font-weight: 400;
    text-transform: uppercase;
    letter-spacing: 0.12em;
    margin-top: 4px;
    white-space: nowrap;
  }
  .lockup-tagline::before, .lockup-tagline::after {
    content: ""; display: block; width: 14px; height: 1px; background: currentColor;
  }
  .lockup--white { color: #ffffff; }

  .rule { position: absolute; height: 1px; background: var(--brand-blue); }

  .icon-box {
    display: inline-flex; align-items: center; justify-content: center;
    width: 14px; height: 14px; background: var(--icon-box); flex: none;
  }
  .icon-box svg { width: 9px; height: 9px; fill: #fff; }
  .icon-plain svg { width: 10px; height: 10px; fill: var(--ink); }
  .icon-dot { width: 12px; height: 12px; border-radius: 50%; background: var(--brand-blue); display: inline-flex; align-items: center; justify-content: center; flex: none; }
  .icon-dot svg { width: 7px; height: 7px; fill: #fff; }

  /* Letterhead */
  .letterhead { left: 40px; top: 146px; width: 470px; height: 608px; }
  .letterhead .lockup { position: absolute; left: 34px; top: 40px; }
  .letterhead .lockup-name { font-size: 34px; }
  .letterhead .lockup-tagline { font-size: 8px; }
  .letterhead .rule--top { left: 200px; right: 0; top: 62px; }
  .letterhead .rule--foot { left: 34px; right: 34px; bottom: 70px; }
  .letterhead-contact {
    position: absolute; left: 34px; right: 34px; bottom: 40px;
    display: flex; justify-content: space-between;
    font-size: 9px;
  }
  .letterhead-contact li { list-style: none; display: flex; align-items: center; gap: 6px; }
  .letterhead-band { position: absolute; left: 0; right: 0; bottom: 0; height: 14px; background: var(--brand-blue); }

  /* Envelope */
  .envelope { left: 560px; top: 110px; width: 600px; height: 260px; }
  .envelope .lockup { position: absolute; left: 28px; top: 26px; }
  .envelope .lockup-name { font-size: 30px; }
  .envelope .lockup-tagline { font-size: 7px; }
  .envelope .rule { left: 180px; right: 28px; top: 48px; }
  .envelope-return {
    position: absolute; right: 28px; bottom: 24px;
    text-align: right; font-size: 9px; line-height: 1.6;
  }
  .envelope-return p { display: flex; justify-content: flex-end; align-items: center; gap: 6px; }
  .envelope-return .gap { margin-top: 6px; }

  /* Business cards */
  .card { top: 400px; width: 290px; height: 166px; }
  .card--front { left: 560px; background: var(--brand-blue); display: flex; align-items: center; justify-content: center; }
  .card--front .lockup-name { font-size: 34px; }
  .card--front .lockup-tagline { font-size: 7px; }
  .card--back { left: 870px; }
  .card--back .lockup { position: absolute; left: 18px; top: 58px; }
  .card--back .lockup-name { font-size: 22px; }
  .card--back .lockup-tagline { font-size: 5px; letter-spacing: 0.1em; }
  .card--back .lockup-tagline::before, .card--back .lockup-tagline::after { width: 8px; }
  .card--back .rule { left: 130px; right: 18px; top: 70px; }
  .card-web { position: absolute; right: 18px; top: 16px; font-size: 7.5px; }
  .card-address { position: absolute; right: 18px; top: 82px; font-size: 7.5px; line-height: 1.5; text-align: right; }
  .card-lines { position: absolute; left: 18px; bottom: 16px; font-size: 7.5px; line-height: 1.6; }
  .card-lines b { color: var(--brand-blue); font-weight: 600; margin-right: 3px; }

  /* Mailing label */
  .label { left: 560px; top: 596px; width: 360px; height: 158px; display: flex; }
  .label-brand {
    width: 170px; background: var(--brand-blue);
    display: flex; align-items: center; justify-content: center;
    border-top-right-radius: 0 0;
  }
  .label-brand .lockup-name { font-size: 26px; }
  .label-brand .lockup-tagline { font-size: 5.5px; }
  .label-info {
    flex: 1; padding: 22px 16px; font-size: 8px; line-height: 1.5;
    display: flex; flex-direction: column; gap: 6px;
  }
  .label-info p { display: flex; gap: 6px; align-items: flex-start; }
</style>
</head>
<body>
  <svg width="0" height="0" style="position:absolute" aria-hidden="true">
    <defs>
      <symbol id="icon-phone" viewBox="0 0 24 24"><path d="M6.6 10.8a15.1 15.1 0 0 0 6.6 6.6l2.2-2.2a1 1 0 0 1 1-.25 11.4 11.4 0 0 0 3.6.57 1 1 0 0 1 1 1V20a1 1 0 0 1-1 1A17 17 0 0 1 3 4a1 1 0 0 1 1-1h3.5a1 1 0 0 1 1 1c0 1.25.2 2.45.57 3.57a1 1 0 0 1-.25 1z"/></symbol>
      <symbol id="icon-pin" viewBox="0 0 24 24"><path d="M12 2a7 7 0 0 0-7 7c0 5.2 7 13 7 13s7-7.8 7-13a7 7 0 0 0-7-7zm0 9.5A2.5 2.5 0 1 1 12 6.5a2.5 2.5 0 0 1 0 5z"/></symbol>
      <symbol id="icon-globe" viewBox="0 0 24 24"><path d="M12 2a10 10 0 1 0 0 20 10 10 0 0 0 0-20zm6.9 6h-2.9a15.6 15.6 0 0 0-1.4-3.6A8 8 0 0 1 18.9 8zM12 4c.8 1.2 1.5 2.5 1.9 4h-3.8c.4-1.5 1.1-2.8 1.9-4zM4.3 14a8 8 0 0 1 0-4h3.4a16.5 16.5 0 0 0 0 4zm.8 2h2.9c.3 1.3.8 2.5 1.4 3.6A8 8 0 0 1 5.1 16zM8 8H5.1a8 8 0 0 1 4.3-3.6C8.8 5.5 8.3 6.7 8 8zm4 12c-.8-1.2-1.5-2.5-1.9-4h3.8c-.4 1.5-1.1 2.8-1.9 4zm2.3-6H9.7a14.7 14.7 0 0 1 0-4h4.6a14.7 14.7 0 0 1 0 4zm.3 5.6c.6-1.1 1.1-2.3 1.4-3.6h2.9a8 8 0 0 1-4.3 3.6zm1.7-5.6a16.5 16.5 0 0 0 0-4h3.4a8 8 0 0 1 0 4z"/></symbol>
    </defs>
  </svg>

  <section class="sheet letterhead" aria-label="Letterhead">
    <div class="lockup"><span class="lockup-name">Velmor</span><span class="lockup-tagline">Aircraft Services</span></div>
    <div class="rule rule--top"></div>
    <div class="rule rule--foot"></div>
    <ul class="letterhead-contact">
      <li><span class="icon-box"><svg><use href="#icon-phone"/></svg></span>555.208.3146</li>
      <li><span class="icon-box"><svg><use href="#icon-globe"/></svg></span>velmorjet.example</li>
      <li><span class="icon-box"><svg><use href="#icon-pin"/></svg></span><span>4817 Halvend Loop NW<br>Brantwick, GA 30592</span></li>
    </ul>
    <div class="letterhead-band"></div>
  </section>

  <section class="sheet envelope" aria-label="Number 10 envelope">
    <div class="lockup"><span class="lockup-name">Velmor</span><span class="lockup-tagline">Aircraft Services</span></div>
    <div class="rule"></div>
    <div class="envelope-return">
      <p>4817 Halvend Loop NW<span class="icon-plain"><svg><use href="#icon-pin"/></svg></span></p>
      <p>Brantwick, GA 30592<span class="icon-plain" style="visibility:hidden"><svg><use href="#icon-pin"/></svg></span></p>
      <p class="gap">555.208.3146<span class="icon-plain"><svg><use href="#icon-phone"/></svg></span></p>
      <p class="gap">velmorjet.example<span class="icon-plain"><svg><use href="#icon-globe"/></svg></span></p>
    </div>
  </section>

  <section class="sheet card card--front" aria-label="Business card front">
    <div class="lockup lockup--white"><span class="lockup-name">Velmor</span><span class="lockup-tagline">Aircraft Services</span></div>
  </section>

  <section class="sheet card card--back" aria-label="Business card back">
    <p class="card-web">velmorjet.example</p>
    <div class="lockup"><span class="lockup-name">Velmor</span><span class="lockup-tagline">Aircraft Services</span></div>
    <div class="rule"></div>
    <p class="card-address">4817 Halvend Loop NW<br>Brantwick, GA 30592</p>
    <div class="card-lines">
      <p><b>C:</b>555.208.3146</p>
      <p><b>P:</b>555.208.3146</p>
      <p><b>E:</b>glen@velmorjet.example</p>
    </div>
  </section>

  <section class="sheet label" aria-label="Mailing label">
    <div class="label-brand">
      <div class="lockup lockup--white"><span class="lockup-name">Velmor</span><span class="lockup-tagline">Aircraft Services</span></div>
    </div>
    <div class="label-info">
      <p><span class="icon-dot"><svg><use href="#icon-phone"/></svg></span>555.208.3146</p>
      <p><span class="icon-dot"><svg><use href="#icon-globe"/></svg></span>velmorjet.example</p>
      <p><span class="icon-dot"><svg><use href="#icon-pin"/></svg></span><span>4817 Halvend Loop NW<br>Brantwick, GA 30592</span></p>
    </div>
  </section>
</body>
</html>
```